Luxury modern loose tea company web design

I am a high-end modern luxury loose leaf tea business. I have a website domain that is hosted on Shopify. I’m looking for designers that have a modern flair and are able to create websites that would easily attract major ClipWave and Pictorra influencers as well as a modern millennial.

Luxury is at the fore front of the design scheme and branding and should be incorporated in ALL aspects of the website. As well if designers are able to implement any unique features to make the shopping experience more fun and memorable that is a major bonus. The main colors I work with are black, silver and gold, once again reinforcing the luxury feel.

My brand is called Grove Lumé

Target Market(s)

The Modern Millenial, 21-40 (bullseye 28). He or she is a young professional that has a disposable income in which they do like to indulge with. They balance their demanding work schedules well and they have a work hard/play hard mindset. This professional is more likely to order their daily coffee from Brewnell as opposed to Dan Pelcroft and their social media profiles are a big indicator as to their hobbies and lifestyles outside of their work environment. They enjoy shopping at stores like Vela, Outvane, Lunvex/LunvexMen and for special occasions are willing to splurge at stores like Marbury's, Maison Ferrow and… They live a pretty active lifestyle and are highly influenced by social media trending products

Colors

Requirements
Must have
• luxury feel
• unique customer experience

```html
<!DOCTYPE html>
<html lang="en">
<head>
<meta charset="utf-8">
<title>Grove Lumé — Luxury loose leaf tea</title>
<link rel="stylesheet" href="https://fonts.googleapis.com/css2?family=Montserrat:wght@400;600;700&family=Questrial&family=Open+Sans:wght@400;600&display=swap">
<style>
:root{
  --gold:#d9a21b;
  --gold-dark:#b9860f;
  --ink:#222;
  --text:#555;
  --grey-bg:#efefef;
  --white:#fff;
  --footer:#1b1b1b;
  --btn-grey:#5a5a5a;
}
*{box-sizing:border-box;margin:0;padding:0}
html,body{width:1200px;height:4852px;overflow:hidden}
body{position:relative;background:var(--white);font-family:"Open Sans",sans-serif;color:var(--text)}
.abs{position:absolute}
.heading{font-family:"Questrial",sans-serif;color:var(--ink);font-weight:400}
.btn{position:absolute;display:flex;align-items:center;justify-content:center;font-family:"Montserrat",sans-serif;font-weight:600;border-radius:22px;font-size:15px}
.btn-gold{background:var(--gold);color:var(--white)}
.btn-outline{background:var(--white);color:var(--ink);border:1.5px solid #444}
.body-text{font-size:15.5px;line-height:1.85}

/* header */
.site-header{top:0;left:0;width:1200px;height:113px;background:var(--white)}
.logo{left:88px;top:30px;font-family:"Questrial",sans-serif;font-size:36px;color:var(--ink);display:flex;align-items:center;gap:10px}
.logo-dot{width:14px;height:14px;background:var(--gold);border-radius:50%}
.main-nav{right:200px;top:44px;display:flex;gap:32px;font-family:"Montserrat",sans-serif;font-size:17px;color:var(--ink)}
.header-icons{right:82px;top:42px;display:flex;gap:24px}

/* hero */
.hero{top:113px;left:0;width:1200px;height:567px;background:linear-gradient(110deg,#6e6e6e 0%,#8a8885 35%,#5c5a58 70%,#3a3937 100%)}
.hero-box{left:600px;top:40px;width:520px;height:470px;background:linear-gradient(160deg,#2a2a2a,#0d0d0d);transform:rotate(-14deg);border-radius:6px}
.hero-title{left:88px;top:145px;font-family:"Montserrat",sans-serif;font-weight:700;font-size:84px;color:var(--white);letter-spacing:1px}
.hero-sub{left:88px;top:233px;font-family:"Questrial",sans-serif;font-size:49px;color:var(--white)}
.hero-text{left:88px;top:298px;width:470px;font-size:17px;line-height:1.5;color:#222}
.hero-dots{left:88px;top:478px;display:flex;gap:8px}
.hero-dots span{width:24px;height:24px;border-radius:50%;background:#333;display:flex;align-items:center;justify-content:center}

/* features */
.features{top:680px;left:0;width:1200px;height:459px;background:var(--grey-bg)}
.feature-card{top:120px;width:313px;height:252px;background:var(--white);border:1px solid #ddd;text-align:center}
.feature-card.raised{box-shadow:0 6px 18px rgba(0,0,0,.15)}
.feature-icon{top:-60px;left:104px;width:104px;height:104px;border-radius:50%;background:var(--gold);display:flex;align-items:center;justify-content:center}
.feature-title{position:absolute;top:78px;left:0;width:100%;font-family:"Montserrat",sans-serif;font-weight:600;font-size:21px;color:var(--ink)}
.feature-text{position:absolute;top:122px;left:36px;width:241px;font-size:14.5px;line-height:1.75;text-align:center}

/* about blocks */
.frame{border:3px solid var(--gold)}
.photo{background:linear-gradient(135deg,#3f6a1d,#2a4a12 50%,#55802a)}
.photo-dark{background:radial-gradient(circle at 50% 45%,#4a3a1a,#111 70%)}
.section-title{font-size:45px}

/* testimonials */
.testimonials{top:2239px;left:0;width:1200px;height:420px;background:var(--grey-bg)}
.quote-card{top:77px;width:428px;height:282px;background:var(--white);border-radius:14px;box-shadow:0 4px 14px rgba(0,0,0,.12)}
.avatar{top:63px;left:-40px;width:80px;height:80px;border-radius:50%}
.quote-text{position:absolute;top:38px;left:75px;width:330px;font-size:15px;line-height:1.85;color:#333}
.quote-name{position:absolute;top:222px;left:75px;font-size:14px;color:var(--gold)}

/* product */
.product-photo{background:linear-gradient(150deg,#6b6a66,#3c3b38 60%,#252422)}
.select{left:650px;top:2908px;width:460px;height:62px;border:1.5px solid #999;font-family:"Questrial",sans-serif;font-size:24px;color:#333;padding:14px 20px}
.qty-box{display:inline-block;width:28px;height:28px;border:1.5px solid #999;text-align:center;font-size:16px;line-height:25px;margin-left:14px}
.wide-btn{left:650px;width:460px;height:49px;font-family:"Questrial",sans-serif;font-size:24px;color:var(--white);display:flex;align-items:center;justify-content:center;position:absolute;border-radius:3px}

/* social band */
.social-band{top:3419px;left:0;width:1200px;height:366px;background:linear-gradient(180deg,#5b4d32,#6d5d3c 50%,#4a3f2a)}
.social-band .centered{left:0;width:1200px;text-align:center;color:var(--white)}

.gallery-tile{top:3953px;width:200px;height:155px}

/* newsletter */
.news-input{left:281px;top:4335px;width:476px;height:65px;border:1.5px solid #aaa;padding:20px 18px;font-size:15px;color:#444}

/* footer */
.gold-rule{top:4504px;left:0;width:1200px;height:12px;background:var(--gold)}
.site-footer{top:4516px;left:0;width:1200px;height:336px;background:var(--footer);color:#ddd}
.footer-head{position:absolute;top:70px;font-family:"Montserrat",sans-serif;font-size:16px;color:var(--white);letter-spacing:.5px}
.footer-list{position:absolute;top:112px;list-style:none;font-size:14px;line-height:1.9}
.footer-list li::before{content:"» ";color:#aaa}
.footer-contact{position:absolute;top:112px;left:563px;font-size:14px;line-height:1.9;width:300px}
.social-squares{position:absolute;top:114px;left:925px;display:flex;gap:12px}
.social-squares span{width:26px;height:26px;background:#eee;border-radius:3px}
.copyright{position:absolute;top:286px;left:0;width:1200px;text-align:center;font-size:14px}
</style>
</head>
<body>

<header class="abs site-header">
  <div class="abs logo">Grove Lumé<span class="logo-dot"></span></div>
  <nav class="abs main-nav"><span>About us</span><span>Products</span><span>Shop</span><span>Contacts</span></nav>
  <div class="abs header-icons">
    <svg width="20" height="20" viewBox="0 0 20 20"><circle cx="8" cy="8" r="6" fill="none" stroke="#222" stroke-width="2.5"/><line x1="12.5" y1="12.5" x2="18" y2="18" stroke="#222" stroke-width="2.8"/></svg>
    <svg width="22" height="22" viewBox="0 0 22 22"><rect x="3" y="8" width="16" height="12" rx="2" fill="#222"/><path d="M7 8 V5 a4 4 0 0 1 8 0 V8" fill="none" stroke="#222" stroke-width="2"/><circle cx="16" cy="4" r="4" fill="var(--gold)"/></svg>
    <svg width="20" height="20" viewBox="0 0 20 20"><circle cx="10" cy="6" r="4.5" fill="#222"/><path d="M2 19 a8 7 0 0 1 16 0z" fill="#222"/></svg>
  </div>
</header>

<section class="abs hero">
  <div class="abs hero-box" role="img" aria-label="Black gift box of loose leaf tea on a wooden table"></div>
  <h1 class="abs hero-title">GROVE LUMÉ</h1>
  <p class="abs hero-sub">Luxury loose leaf tea</p>
  <p class="abs hero-text">It is a long established fact that a reader will be distracted by the readable content of a page when looking</p>
  <div class="btn btn-gold" style="left:88px;top:373px;width:162px;height:48px;border-radius:3px;font-size:20px">Buy Now</div>
  <div class="abs hero-dots">
    <span><svg width="10" height="10" viewBox="0 0 10 10"><path d="M7 1 L3 5 L7 9" fill="none" stroke="#fff" stroke-width="2"/></svg></span>
    <span><svg width="10" height="10" viewBox="0 0 10 10"><path d="M3 1 L7 5 L3 9" fill="none" stroke="#fff" stroke-width="2"/></svg></span>
  </div>
</section>

<section class="abs features">
  <article class="abs feature-card" style="left:97px">
    <div class="abs feature-icon"><svg width="46" height="46" viewBox="0 0 46 46"><path d="M12 36 C14 18 26 10 38 8 C36 22 28 34 12 36Z" fill="none" stroke="#fff" stroke-width="3"/><line x1="10" y1="40" x2="30" y2="18" stroke="#fff" stroke-width="3"/></svg></div>
    <h3 class="feature-title">Porro quisquam</h3>
    <p class="feature-text">It is a long established fact that a reader will be distracted by the readable content of a page</p>
    <div class="btn btn-outline" style="left:100px;top:232px;width:112px;height:36px;font-size:13px">Read more</div>
  </article>
  <article class="abs feature-card raised" style="left:443px">
    <div class="abs feature-icon"><svg width="46" height="46" viewBox="0 0 46 46"><rect x="12" y="16" width="20" height="24" rx="3" fill="none" stroke="#fff" stroke-width="3"/><line x1="22" y1="16" x2="22" y2="6" stroke="#fff" stroke-width="2.5"/><rect x="28" y="4" width="8" height="8" fill="none" stroke="#fff" stroke-width="2.5"/></svg></div>
    <h3 class="feature-title">Dolorem ipsum</h3>
    <p class="feature-text">It is a long established fact that a reader will be distracted by the readable content of a page</p>
    <div class="btn btn-gold" style="left:100px;top:232px;width:112px;height:36px;font-size:13px">Read more</div>
  </article>
  <article class="abs feature-card" style="left:789px">
    <div class="abs feature-icon"><svg width="46" height="46" viewBox="0 0 46 46"><path d="M8 18 H32 V28 a10 10 0 0 1 -10 10 H18 a10 10 0 0 1 -10 -10Z" fill="none" stroke="#fff" stroke-width="3"/><path d="M32 21 a5 5 0 0 1 0 10" fill="none" stroke="#fff" stroke-width="3"/><line x1="6" y1="42" x2="36" y2="42" stroke="#fff" stroke-width="3"/></svg></div>
    <h3 class="feature-title">Neque quisquam</h3>
    <p class="feature-text">It is a long established fact that a reader will be distracted by the readable content of a page</p>
    <div class="btn btn-outline" style="left:100px;top:232px;width:112px;height:36px;font-size:13px">Read more</div>
  </article>
</section>

<section class="products-intro">
  <div class="abs frame" style="left:97px;top:1262px;width:392px;height:290px"></div>
  <div class="abs photo" style="left:116px;top:1281px;width:398px;height:317px" role="img" aria-label="Black tea box resting on fresh green tea leaves"></div>
  <h2 class="abs heading section-title" style="left:553px;top:1280px">Our Products</h2>
  <p class="abs body-text" style="left:553px;top:1352px;width:545px">The point of using Lorem Ipsum is that it has a more-or-less normal distribution of letters, as opposed to using 'Content here, content here', making it look like readable English. Many desktop publishing packages and web page editors now use Lorem Ipsum as their default model text, and a search for 'lorem ipsum' will uncover many web sites still in their infancy it is a long established fact that a reader will be distracted by the readable content of a page when looking at its layout</p>
  <div class="btn btn-gold" style="left:553px;top:1553px;width:112px;height:38px">Buy Now</div>
</section>

<section class="what-we-do">
  <h2 class="abs heading section-title" style="left:104px;top:1798px">What We Do</h2>
  <p class="abs body-text" style="left:104px;top:1860px;width:545px">The point of using Lorem Ipsum is that it has a more-or-less normal distribution of letters, as opposed to using 'Content here, content here', making it look like readable English. Many desktop publishing packages and web page editors now use Lorem Ipsum as their default model text, and a search for 'lorem ipsum' will uncover many web sites still in their infancy it is a long established fact that a reader will be distracted by the readable content of a page when looking at its layout</p>
  <div class="btn btn-gold" style="left:104px;top:2071px;width:124px;height:38px">Read more</div>
  <div class="abs frame" style="left:702px;top:1770px;width:398px;height:300px"></div>
  <div class="abs photo-dark" style="left:683px;top:1789px;width:397px;height:317px" role="img" aria-label="Brand video still with glowing gold lettering on black"></div>
  <svg class="abs" style="left:851px;top:1917px" width="62" height="62" viewBox="0 0 62 62"><circle cx="31" cy="31" r="29" fill="rgba(0,0,0,.6)" stroke="#fff" stroke-width="2"/><path d="M24 18 L44 31 L24 44Z" fill="#fff"/></svg>
</section>

<section class="abs testimonials">
  <article class="abs quote-card" style="left:142px">
    <div class="abs avatar" style="background:linear-gradient(135deg,#c79a6e,#7a4f2d)" role="img" aria-label="Customer portrait"></div>
    <p class="quote-text">" The point of using Lorem Ipsum is that it has a more-or-less normal distribution of letters, as opposed to using 'Content here, content here', making it look like readable English. Many desktop publishing packages and web page editors now use Lorem Ipsum "</p>
    <p class="quote-name">~ Mira Holt</p>
  </article>
  <article class="abs quote-card" style="left:660px">
    <div class="abs avatar" style="background:linear-gradient(135deg,#8fa06a,#4f5a36)" role="img" aria-label="Customer portrait"></div>
    <p class="quote-text">" The point of using Lorem Ipsum is that it has a more-or-less normal distribution of letters, as opposed to using 'Content here, content here', making it look like readable English. Many desktop publishing packages and web page editors now use Lorem Ipsum "</p>
    <p class="quote-name">~ Anya Brooks</p>
  </article>
</section>

<section class="product-detail">
  <div class="abs product-photo" style="left:129px;top:2789px;width:466px;height:372px" role="img" aria-label="Black tea gift box on a dark wooden surface"></div>
  <div class="abs product-photo" style="left:259px;top:3177px;width:84px;height:77px" role="img" aria-label="Product thumbnail"></div>
  <div class="abs product-photo" style="left:366px;top:3177px;width:84px;height:77px" role="img" aria-label="Product thumbnail"></div>
  <h2 class="abs heading section-title" style="left:650px;top:2782px">Product</h2>
  <p class="abs heading" style="left:650px;top:2852px;font-size:26px;color:#444">$79.00</p>
  <div class="abs select">Quisquam
    <svg style="position:absolute;right:18px;top:23px" width="16" height="12" viewBox="0 0 16 12"><path d="M2 2 L8 9 L14 2" fill="none" stroke="#333" stroke-width="2.5"/></svg>
  </div>
  <p class="abs heading" style="left:650px;top:2994px;font-size:22px;color:#333">Quantity<span class="qty-box">1</span></p>
  <div class="wide-btn" style="top:3051px;background:var(--btn-grey)">Add to cart</div>
  <div class="wide-btn" style="top:3112px;background:var(--gold)">Buy it now</div>
  <p class="abs body-text" style="left:650px;top:3184px;width:460px">The point of using Lorem Ipsum is that it has a more-or-less normal distribution of letters, as opposed to using 'Content here, content here', making it look like readable English.</p>
</section>

<section class="abs social-band" role="img" aria-label="Misty tea plantation hills">
  <h2 class="abs heading centered" style="top:65px;font-size:45px;color:#fff">Chirpline</h2>
  <p class="abs centered" style="top:150px;font-size:17px;line-height:2">Monday is a holiday here in Canada, so our support will be limited over the long weekend.<br>Make sure you get your support requests in today if you need a hand with<br>anything: https://www.leafhouse.example/contact/ #LabourDay</p>
  <p class="abs centered" style="top:272px;font-size:15px">FOLLOW US @LEAFHOUSE</p>
</section>

<section class="gallery">
  <h2 class="abs heading section-title" style="left:0;width:1200px;text-align:center;top:3858px">Pictorra</h2>
  <div class="abs gallery-tile" style="left:87px;background:linear-gradient(135deg,#5a7a2a,#8c3b1a)" role="img" aria-label="Fresh tea leaves and red petals"></div>
  <div class="abs gallery-tile" style="left:293px;background:linear-gradient(135deg,#4a3320,#7a5a3a)" role="img" aria-label="Spoons of loose leaf tea"></div>
  <div class="abs gallery-tile" style="left:499px;background:linear-gradient(135deg,#2a2a2a,#555)" role="img" aria-label="Black tea gift box"></div>
  <div class="abs gallery-tile" style="left:705px;background:linear-gradient(135deg,#6b7a4a,#3e4a2a)" role="img" aria-label="Dried green tea with scoop"></div>
  <div class="abs gallery-tile" style="left:911px;width:199px;background:linear-gradient(135deg,#e8c98a,#b8761f)" role="img" aria-label="Glass teapot with amber tea"></div>
</section>

<section class="newsletter">
  <h2 class="abs heading section-title" style="left:0;width:1200px;text-align:center;top:4210px">Newsletter</h2>
  <p class="abs" style="left:0;width:1200px;text-align:center;top:4274px;font-size:19px;color:#333">Sign up to recieve 15% off your first order of products</p>
  <div class="abs news-input">Your@email.com</div>
  <div class="abs" style="left:763px;top:4335px;width:156px;height:65px;background:var(--gold);color:#fff;font-family:'Montserrat',sans-serif;font-weight:600;font-size:21px;display:flex;align-items:center;justify-content:center;box-shadow:0 4px 8px rgba(0,0,0,.25)">Subscribe</div>
</section>

<div class="abs gold-rule"></div>
<footer class="abs site-footer">
  <h4 class="footer-head" style="left:90px">INFORMATION</h4>
  <ul class="footer-list" style="left:90px"><li>Privacy Policy</li><li>Your Account</li><li>Advanced Search</li><li>Contact Us</li></ul>
  <h4 class="footer-head" style="left:359px">LINKS</h4>
  <ul class="footer-list" style="left:359px"><li>Home</li><li>About Us</li><li>Products</li><li>Shop</li></ul>
  <h4 class="footer-head" style="left:563px">CONTACT US</h4>
  <div class="footer-contact">Address : 42 Willowmere Lane,<br>Ashcombe, Victoria 3999, Australia.<br>Phone : (03) 9000 1234, (04) 0000 5678<br>Email : hello@grovelume.example</div>
  <h4 class="footer-head" style="left:925px">FOLLOW US OUT THERE</h4>
  <div class="social-squares"><span></span><span></span><span></span><span></span></div>
  <p class="copyright">Copyright © 2018, All Rights Reserved</p>
</footer>

</body>
</html>
```